14 years in business and its time for a new look and feel brochure and business cards!

We are looking to create a brochure that is professional and eye catching to bring in new commercial business. After14 years in business we have finally redone our logo and it is time to get a brochure completed as well. The logo that should be used is the one that says Inc. We want this new brochure to appeal to corporate property management companies and smaller apartment complexes. We want it to look rich and have the same high quality our work has.

Target Market(s)

property management companies and apartment complexes in the DMV.

Industry/Entity Type

Construction Company

Contact Information for Business Card

Logo
Dovid Rennick
CEO
Mobile 410-555-0137
Office 410-555-0192
Address 3817 Larchmont Lane Suite B Baltimore, MD 21208
Email DR@BrightCoatInc.example

Font styles to use
Sans Serif

Requirements
Must have
• Want the background to be black and silver gradient. Will be printing on high gloss and would like for it to be rich looking.
• brochure will be 8.5x11. open minded in terms of the fold, how it looks best with the design provided will determine that. Can be bi-fold, try-fold or z-fold.
• Content for brochure:About us
• Founded in 2003, The Bright Coat Inc. was the vision of Dovid Rennick, with a commitment to becoming the premier renovator and developer of residential and commercial properties in the DMV. Today, The Bright Coat Inc. is widely respected for their gold standard in quality and efficiency and continues to grow by attracting the highest level of professionals with knowledge and experience in our field.
• The Bright Coat Inc.’s most valuable asset is our team members. The efforts they put forth are the key to meeting our standards and providing all of our valued clients with the highest quality of service. Leading our wonderful team members is a group of management like no other. With years of experience, the power to motivate and the keen eye to ensure top quality, our team of experts focus all of their energy to exceed our client’s expectations.
• Our Mission
• We strive to provide timely delivery, the highest level of quality and value on every project. We offer unsurpassed dedication to maintain our working relationships and consistently deliver the best service to ensure our clients success.
• Property Renovations
• The Bright Coat Inc. has been responsible for coordinating the construction and renovation of many projects, including all parts of a building’s interior and exterior. Well known for attention to details, quality and timely execution, The Bright Coat Inc. has managed and executed more than 4,000 turnovers and over 150 projects in the last 3 years alone.
• Renovations not only improve the appeal and marketability of your property, but also add value. Interior and exterior renovations help make any property more functional, energy-efficient and enable you to keep up with what your market demands. From the smallest change of a door knob to a complete kitchen overhaul, these are the things that make all the difference in your property. We are committed to deliver great value, and we do that by ensuring that our experts are involved in the renovation process, providing input and quality maintenance throughout the entire renovation.
• Services Include
• Painting
• Flooring
• Sub-Flooring
• Crown molding
• Siding & Wood Replacement
• Trim & Carpentry Work
• Punches
• Decks
• Power wash
• Concrete & Paving
• Turnovers including plumbing and electric
• Kitchen overhauls
• We offer first time clients a free apartment paint or punch on us to show you the quality you can always expect!
• Call today to schedule your first-time paint or punch at 410-555-0192.

```html
<!DOCTYPE html>
<html lang="en">
<head>
<meta charset="utf-8">
<title>The Bright Coat Inc. – Brochure Covers</title>
<link rel="stylesheet" href="https://fonts.googleapis.com/css2?family=Montserrat:wght@600;800&family=Open+Sans:wght@400;600&display=swap">
<style>
  :root {
    --backdrop: #d9dadd;
    --paper-light: #fbfbfd;
    --paper-mid: #e9eaef;
    --paper-shade: #d6d8e0;
    --ink-dark: #2b2c30;
    --ink-mid: #55575d;
    --ink-soft: #8a8c93;
    --pill-top: #5a5b60;
    --pill-bottom: #1f2023;
    --rule: #9c9ea5;
    --sky-top: #5d6fa8;
    --sky-mid: #8e8fb4;
    --city-warm: #a0704a;
  }
  * { box-sizing: border-box; margin: 0; padding: 0; }
  html, body { width: 1200px; height: 789px; overflow: hidden; }
  body {
    background: var(--backdrop);
    font-family: "Open Sans", sans-serif;
    display: flex; align-items: center; justify-content: center;
  }
  .spread { display: flex; width: 1082px; height: 700px; box-shadow: 0 10px 30px rgba(0,0,0,.25); }
  .page { position: relative; width: 541px; height: 700px; overflow: hidden; }
  .page--back {
    background: linear-gradient(160deg, var(--paper-light) 0%, var(--paper-mid) 55%, var(--paper-shade) 100%);
    border-right: 1px solid #c6c8cf;
  }
  .page--front {
    background: linear-gradient(200deg, var(--paper-light) 0%, var(--paper-mid) 60%, var(--paper-shade) 100%);
  }
  .brand-name {
    position: absolute; display: flex; align-items: center; gap: 12px;
    font-family: "Montserrat", sans-serif; font-weight: 800;
    color: var(--ink-mid); letter-spacing: 1px; white-space: nowrap;
  }
  .brand-name .dot { width: 22px; height: 22px; border-radius: 50%; background: var(--ink-mid); }
  .page--back .brand-name { left: 50%; top: 250px; transform: translateX(-50%); font-size: 30px; }
  .offer-box {
    position: absolute; left: 58px; right: 58px; top: 418px;
    border: 1px solid var(--rule); padding: 34px 22px 22px; text-align: center;
  }
  .offer-label {
    position: absolute; top: -22px; left: 50%; transform: translateX(-50%);
    background: linear-gradient(var(--pill-top), var(--pill-bottom));
    color: #fff; font-family: "Montserrat", sans-serif; font-weight: 800;
    font-size: 26px; padding: 4px 28px; white-space: nowrap;
  }
  .offer-headline { font-family: "Montserrat", sans-serif; font-weight: 800; font-size: 15px; color: var(--ink-dark); }
  .offer-text { font-size: 13px; color: var(--ink-dark); margin-top: 4px; line-height: 1.35; }
  .phone-pill {
    display: inline-flex; align-items: center; gap: 12px;
    background: linear-gradient(var(--pill-top), var(--pill-bottom));
    color: #fff; font-family: "Montserrat", sans-serif; font-weight: 800;
    border-radius: 30px; box-shadow: 0 3px 6px rgba(0,0,0,.3);
  }
  .phone-pill svg { fill: none; stroke: #fff; stroke-width: 1.6; }
  .offer-box .phone-pill { margin-top: 16px; font-size: 26px; padding: 8px 28px 8px 20px; }
  .website {
    position: absolute; left: 0; right: 0; top: 640px; text-align: center;
    font-size: 14px; color: var(--ink-dark);
    display: flex; justify-content: center; align-items: center; gap: 8px;
  }
  .website svg { fill: none; stroke: var(--ink-dark); stroke-width: 1.4; }
  .cover-photo {
    position: absolute; left: 60px; top: 40px; width: 450px; height: 460px;
    border-radius: 50%;
    background: linear-gradient(200deg, var(--sky-top) 0%, var(--sky-mid) 45%, #4b4e62 70%, var(--city-warm) 100%);
    border: 14px solid #b9bbc2;
  }
  .page--front .brand-name { left: 110px; top: 560px; font-size: 26px; }
  .page--front .phone-pill { position: absolute; right: 30px; top: 612px; font-size: 16px; padding: 7px 18px 7px 14px; }
</style>
</head>
<body>
  <main class="spread">
    <section class="page page--back">
      <div class="brand-name"><span class="dot"></span>THE BRIGHT COAT INC</div>
      <div class="offer-box">
        <div class="offer-label">WE OFFER</div>
        <p class="offer-headline">FIRST TIME CLIENTS A FREE APARTMENT PAINT</p>
        <p class="offer-text">or punch on us to show you the quality you can always expect!<br>Call today to schedule your first-time paint or punch at</p>
        <div class="phone-pill">
          <svg width="24" height="24" viewBox="0 0 24 24"><circle cx="12" cy="12" r="10.5"/><path d="M8.5 7.5l2 2-1 1.5c.7 1.4 1.6 2.3 3 3l1.5-1 2 2-1.3 1.5c-3.5-.5-6.2-3.2-6.7-6.7z"/></svg>
          410-555-0192
        </div>
      </div>
      <div class="website">
        <svg width="14" height="14" viewBox="0 0 14 14"><circle cx="7" cy="7" r="6"/><path d="M1 7h12M7 1c-2.5 3-2.5 9 0 12M7 1c2.5 3 2.5 9 0 12"/></svg>
        www.brightcoatinc.example
      </div>
    </section>
    <section class="page page--front">
      <div class="cover-photo" role="img" aria-label="Photograph of downtown high-rise apartment towers at dusk, seen from street level"></div>
      <div class="brand-name"><span class="dot"></span>THE BRIGHT COAT INC</div>
      <div class="phone-pill">
        <svg width="16" height="16" viewBox="0 0 24 24"><circle cx="12" cy="12" r="10.5"/><path d="M8.5 7.5l2 2-1 1.5c.7 1.4 1.6 2.3 3 3l1.5-1 2 2-1.3 1.5c-3.5-.5-6.2-3.2-6.7-6.7z"/></svg>
        410-555-0192
      </div>
    </section>
  </main>
</body>
</html>
```